Custom Apparel Decorating Company needs a Website Home Page Banner Design

We are in need of a website Home page banner design for a small company based in Canada called Quelvana. We are a custom apparel company that offers custom apparel (t-shirts, hoodies, hats etc) to Companies, Organizations/groups, bands, Spirit wear and individuals. We would like the design to match with the logo files we have attached to the campaign. The Website has not been created yet planning to tie the website into the home page banner for flow. Thinking of using Duda or Shopify for the website if that helps! We are really looking forward to seeing the designs.

Target Market(s)

Companies, Organizations/Groups, Bands, Spirit wear and Individuals. Anyone that is looking to have there company or own logo/Design put on a piece of clothing.

Requirements
Must have
• -Colours in the logo files.
• -FUN creating the Home Page Banner!!! :)
Nice to have
• -Up Beat feel to it (it's the first image you will see when you go to the website, it's the store front so we want to grab the attention of the potential customers)

```html
<!DOCTYPE html>
<html lang="en">
<head>
<meta charset="utf-8">
<title>Quelvana Apparel – Home Banner</title>
<link href="https://fonts.googleapis.com/css2?family=Ubuntu:wght@400;500;700&display=swap" rel="stylesheet">
<style>
  :root {
    --page-bg: #d9d9d9;
    --banner-dark: #1f1f1f;
    --banner-mid: #2e2e2e;
    --frame-white: #ffffff;
    --text-white: #ffffff;
    --button-blue: #4a72b8;
    --shadow: rgba(0, 0, 0, 0.35);
  }
  * { box-sizing: border-box; margin: 0; padding: 0; }
  html, body {
    width: 1200px;
    height: 1200px;
    overflow: hidden;
    background: var(--page-bg);
    font-family: "Ubuntu", sans-serif;
  }
  .banner {
    position: absolute;
    left: 20px;
    top: 166px;
    width: 1160px;
    height: 869px;
    border: 5px solid var(--frame-white);
    box-shadow: 0 4px 14px var(--shadow);
    overflow: hidden;
  }
  .banner-backdrop {
    position: absolute;
    inset: 0;
    background:
      radial-gradient(ellipse 45% 70% at 55% 45%, #3a3a3a 0%, rgba(58,58,58,0) 70%),
      linear-gradient(180deg, var(--banner-mid) 0%, var(--banner-dark) 100%);
  }
  .brand {
    position: absolute;
    top: 26px;
    left: 0;
    width: 100%;
    display: flex;
    flex-direction: column;
    align-items: center;
    gap: 14px;
    color: var(--text-white);
  }
  .brand-square {
    width: 40px;
    height: 40px;
    background: var(--text-white);
  }
  .brand-name {
    font-size: 24px;
    font-weight: 500;
    letter-spacing: 1px;
  }
  .product-photo {
    position: absolute;
    border: 5px solid var(--frame-white);
    box-shadow: 0 3px 10px rgba(0,0,0,0.45);
  }
  .photo-tee {
    left: 143px;
    top: 151px;
    width: 350px;
    height: 312px;
    transform: rotate(20.7deg);
    background: linear-gradient(135deg, #d4d4d8 0%, #b9b9bf 55%, #8e8e94 100%);
  }
  .photo-hoodie {
    left: 560px;
    top: 279px;
    width: 271px;
    height: 241px;
    background: linear-gradient(180deg, #5a3e2b 0%, #2a2a2a 45%, #1a1a1a 100%);
  }
  .photo-cap {
    left: 855px;
    top: 93px;
    width: 207px;
    height: 182px;
    background: linear-gradient(160deg, #8d8d8d 0%, #5a5a5a 50%, #24324a 100%);
  }
  .headline {
    position: absolute;
    left: 0;
    width: 100%;
    top: 580px;
    text-align: center;
    color: var(--text-white);
    font-size: 73px;
    font-weight: 700;
    letter-spacing: 0.5px;
  }
  .tagline {
    position: absolute;
    left: 0;
    width: 100%;
    top: 692px;
    text-align: center;
    color: var(--text-white);
    font-size: 32px;
    font-weight: 400;
  }
  .shop-button {
    position: absolute;
    left: 479px;
    top: 761px;
    width: 192px;
    height: 60px;
    border: 2px solid var(--frame-white);
    border-radius: 30px;
    background: var(--button-blue);
    color: var(--text-white);
    font-size: 24px;
    font-weight: 500;
    display: flex;
    align-items: center;
    justify-content: center;
  }
</style>
</head>
<body>
  <section class="banner">
    <div class="banner-backdrop" role="img" aria-label="Dark, dimmed photo of a man in a cap and striped long-sleeve shirt"></div>

    <header class="brand">
      <div class="brand-square"></div>
      <div class="brand-name">Quelvana Apparel</div>
    </header>

    <div class="product-photo photo-tee" role="img" aria-label="Photo of a man wearing a white cap and a splatter-print graphic t-shirt"></div>
    <div class="product-photo photo-hoodie" role="img" aria-label="Photo of a black hoodie with grey hood and sleeves on a wooden wall"></div>
    <div class="product-photo photo-cap" role="img" aria-label="Photo of a bearded man adjusting a black and white trucker cap"></div>

    <h1 class="headline">T-shirts, Hoodies, hats etc</h1>
    <p class="tagline">We are a customapparel company that offers custom apparel</p>
    <div class="shop-button">Shop Now</div>
  </section>
</body>
</html>
```